Website - Tides Of Bloom

We are catalysts of change in people's lives.
We work with individuals and professionals to bring about instant substantial & transforming change in their lives.
We provide one-on-one lifestyle coaching by an experienced practitioner.
Our existing website is www.tidesofbloom.biz & this site contains our the basis for the content of our desired new project, so please examine this carefully.
We require a professional and captivating website that will instantly impress, engage invite our readers to click & invest their lives.
Our services do not come cheap, but are second to none.
Our website must be contemporary whilst reflecting indisputable class & ultra-confidence in the success of our work.
Target Market(s)
Those who seek to want to change in their lives. Those aged primarily between 30 and 50 years of age, male or female.
Industry/Entity Type
Work
Look and feel

```html
<!DOCTYPE html>
<html lang="en">
<head>
<meta charset="utf-8">
<title>Tides Of Bloom</title>
<link rel="stylesheet" href="https://fonts.googleapis.com/css2?family=Carlito:wght@400&family=Questrial&family=Arimo:wght@400&display=swap">
<style>
  :root {
    --header-bg: #1f2022;
    --footer-bg: #252525;
    --nav-text: #b9b9b9;
    --nav-active: #ffffff;
    --nav-marker: #3c3c3e;
    --heading-blue: #1b5a89;
    --body-grey: #5a5a5a;
    --accent-orange: #e8601f;
    --accent-green: #3d9b1b;
    --footer-text: #b4b4b4;
    --social-bg: #3a3a3a;
    --white: #ffffff;
  }
  * { margin: 0; padding: 0; box-sizing: border-box; }
  html, body { width: 1200px; height: 856px; overflow: hidden; }
  body { position: relative; background: var(--footer-bg); font-family: "Arimo", Arial, sans-serif; }

  .site-header {
    position: absolute; left: 0; top: 0; width: 1200px; height: 100px;
    background: linear-gradient(#262729, var(--header-bg));
  }
  .brand {
    position: absolute; left: 172px; top: 30px;
    display: flex; align-items: center; gap: 12px;
    font-family: "Questrial", sans-serif; font-size: 26px; color: #d6d6d6;
  }
  .brand-mark { width: 30px; height: 30px; border-radius: 50%; background: #3f7fb8; }
  .main-nav { position: absolute; top: 41px; left: 0; width: 1200px; }
  .main-nav a {
    position: absolute; transform: translateX(-50%);
    font-family: "Questrial", sans-serif; font-size: 15px;
    color: var(--nav-text); text-decoration: none; white-space: nowrap;
  }
  .main-nav a.is-active { color: var(--nav-active); }
  .nav-marker { position: absolute; left: 641px; top: 93px; width: 81px; height: 7px; background: var(--nav-marker); }

  .hero {
    position: absolute; left: 0; top: 100px; width: 1200px; height: 700px;
    background: linear-gradient(180deg, #b9c3cc 0%, #d4dade 30%, #9fb2b5 41%, #4f7f7c 48%, #6d938c 62%, #c9cdc6 78%, #e8dccb 100%);
  }
  .hero-panel {
    position: absolute; left: 156px; top: 115px; width: 396px; height: 396px;
    border-radius: 50%; background: rgba(255,255,255,0.35);
  }
  .hero-panel-inner {
    position: absolute; left: 15px; top: 15px; width: 366px; height: 366px;
    border-radius: 50%; background: rgba(240,242,243,0.72);
    text-align: center;
  }
  .hero-title {
    margin-top: 76px;
    font-family: "Carlito", Calibri, sans-serif; font-weight: 400;
    font-size: 31px; line-height: 40px; color: var(--heading-blue);
  }
  .hero-text {
    margin: 21px auto 0; width: 340px;
    font-size: 13.5px; line-height: 18.5px; color: var(--body-grey);
  }
  .cta-ring {
    position: absolute; left: 105px; top: 295px; width: 188px; height: 50px;
    border-radius: 25px; background: rgba(255,255,255,0.6);
  }
  .cta-button {
    position: absolute; left: 6px; top: 6px; width: 176px; height: 38px;
    border-radius: 19px; background: var(--accent-orange);
    font-family: "Carlito", Calibri, sans-serif; font-size: 18px; line-height: 38px;
    color: var(--white); text-decoration: none;
  }
  .slider-arrow { position: absolute; top: 322px; }
  .slider-arrow.prev { left: 108px; }
  .slider-arrow.next { left: 1071px; }

  .site-footer { position: absolute; left: 0; top: 800px; width: 1200px; height: 56px; background: var(--footer-bg); }
  .copyright { position: absolute; left: 157px; top: 22px; font-size: 11px; color: var(--footer-text); }
  .social-links { position: absolute; left: 652px; top: 12px; display: flex; gap: 6px; }
  .social-links span {
    width: 30px; height: 30px; border-radius: 50%;
    background: var(--social-bg); border: 1px solid #4a4a4a;
  }
  .newsletter { position: absolute; left: 800px; top: 12px; display: flex; height: 33px; }
  .newsletter-field {
    width: 166px; border-radius: 17px 0 0 17px; background: var(--white);
    font-size: 11px; color: #555; line-height: 33px; padding-left: 12px;
  }
  .newsletter-submit {
    width: 78px; border-radius: 0 17px 17px 0; background: var(--accent-green);
    font-family: "Carlito", Calibri, sans-serif; font-size: 15px; color: var(--white);
    line-height: 33px; text-align: center;
  }
</style>
</head>
<body>
  <header class="site-header">
    <div class="brand"><span class="brand-mark"></span><span>Tides Of Bloom</span></div>
    <nav class="main-nav">
      <a class="is-active" href="#" style="left:682px">Home</a>
      <a href="#" style="left:777px">Business</a>
      <a href="#" style="left:885px">Individual</a>
      <a href="#" style="left:1004px">Contact Us</a>
    </nav>
    <div class="nav-marker"></div>
  </header>

  <section class="hero" role="img" aria-label="Photo of a woman with wind-blown hair and outstretched arms on a beach by the sea under a cloudy sky">
    <div class="hero-panel">
      <div class="hero-panel-inner">
        <h1 class="hero-title">We are catalysts of<br>change in people's lives</h1>
        <p class="hero-text">Lorem ipsum dolor sit amet, consectetur adipisicing elit. Accusamus, vero, voluptates at temporibus fugit praesentium eaque aspernatur a ipsam non dolor repellendus blanditiis unde eveniet iusto iure voluptatum ad officiis molestiae sit explicabo.</p>
        <div class="cta-ring"><a class="cta-button" href="#">Learn More</a></div>
      </div>
    </div>
    <svg class="slider-arrow prev" width="22" height="38" viewBox="0 0 22 38"><polyline points="19,2 3,19 19,36" fill="none" stroke="#fff" stroke-width="3"/></svg>
    <svg class="slider-arrow next" width="22" height="38" viewBox="0 0 22 38"><polyline points="3,2 19,19 3,36" fill="none" stroke="#fff" stroke-width="3"/></svg>
  </section>

  <footer class="site-footer">
    <p class="copyright">©2002-2013 Tides Of Bloom. All rights reserved.</p>
    <div class="social-links"><span></span><span></span><span></span><span></span></div>
    <div class="newsletter">
      <div class="newsletter-field">Subscribe to Newsletter</div>
      <div class="newsletter-submit">Submit</div>
    </div>
  </footer>
</body>
</html>
```